Looking for potential sellers

We help people buy and sell homes and are currently looking for potential home sellers. We offer low commissions, are the Local Colorado Springs and Falcon Experts, homes selling fast and at top dollar, Free expert pricing opinions and Consultations, over 9 years of experience, top rated Realtors creative and aggressive marketing strategies. Never merely own a house, THRIVE at Harborview. phone number 482-630-9157 web thriveatharborview.com

```html
<!DOCTYPE html>
<html lang="en">
<head>
<meta charset="utf-8">
<title>Harborview Realty – Seller Postcard</title>
<link href="https://fonts.googleapis.com/css2?family=Poppins:ital,wght@0,300;0,400;0,500;0,600;0,700;1,300&display=swap" rel="stylesheet">
<style>
  :root {
    --olive: #8c8f2e;
    --olive-text: #7d8128;
    --sepia-dark: #4a3a2c;
    --sepia-mid: #7a6250;
    --sepia-light: #a89482;
    --white: #ffffff;
    --ink: #1e1e1e;
    --grey: #8a8a8a;
    --grey-light: #a3a3a3;
    --backdrop: #ececec;
  }
  * { box-sizing: border-box; margin: 0; padding: 0; }
  html, body { width: 1200px; height: 1000px; overflow: hidden; }
  body {
    background: var(--backdrop);
    font-family: "Poppins", sans-serif;
    position: relative;
  }
  .card { position: absolute; width: 720px; height: 480px; overflow: hidden; }

  /* Back card */
  .card-back { left: 63px; top: 443px; background: var(--white); }
  .brand-back {
    position: absolute; left: 30px; top: 30px;
    display: flex; align-items: center; gap: 10px;
    font-size: 28px; font-weight: 500; color: var(--ink);
  }
  .brand-mark { width: 14px; height: 14px; background: var(--olive); }
  .testimonial {
    position: absolute; left: 29px; top: 124px; width: 356px;
    font-size: 13.4px; font-weight: 300; font-style: italic;
    line-height: 20px; color: var(--grey);
  }
  .testimonial-name {
    position: absolute; right: 335px; top: 212px;
    font-size: 13px; font-weight: 600; color: var(--ink);
  }
  .testimonial-meta {
    position: absolute; right: 335px; top: 233px;
    font-size: 11px; font-weight: 400; color: var(--grey-light);
  }
  .home-photos {
    position: absolute; left: 0; top: 267px; width: 385px; height: 75px;
    background: linear-gradient(90deg, #6d7f95 0%, #9a6a4c 40%, #b7a98a 70%, #7d9a5a 100%);
  }
  .rated-band {
    position: absolute; left: 0; top: 342px; width: 385px; height: 91px;
    background: var(--olive);
    display: flex; align-items: center; padding-left: 28px;
    font-size: 31px; font-weight: 700; color: var(--white); letter-spacing: 0.3px;
  }
  .edge-tab {
    position: absolute; right: 0; top: 342px; width: 24px; height: 91px;
    background: var(--olive);
  }

  /* Front card */
  .card-front { left: 423px; top: 85px; }
  .scene {
    position: absolute; inset: 0;
    background: linear-gradient(180deg, var(--sepia-mid) 0%, var(--sepia-light) 35%, var(--sepia-mid) 60%, var(--sepia-dark) 100%);
  }
  .portrait {
    position: absolute; left: 490px; top: 0; width: 230px; height: 480px;
    background: linear-gradient(180deg, #6e5a48 0%, #8a6f5c 45%, #3d3a3f 100%);
  }
  .brand-front {
    position: absolute; left: 34px; top: 92px;
    display: flex; align-items: center; gap: 10px;
    font-size: 32px; font-weight: 500; color: var(--white);
  }
  .selling-points {
    position: absolute; left: 24px; top: 163px; list-style: none;
  }
  .selling-points li {
    height: 30px; display: flex; align-items: center;
    font-size: 15px; font-weight: 400; color: var(--white);
  }
  .selling-points li::before {
    content: "»"; color: #c2c457; font-weight: 700;
    width: 20px; font-size: 17px;
  }
  .selling-points b { font-weight: 600; margin-right: 4px; }
  .selling-points .after { margin-left: 4px; }
  .tagline-band {
    position: absolute; left: 0; top: 343px; width: 512px; height: 90px;
    background: var(--olive);
    padding: 10px 0 0 21px;
    font-size: 26px; font-weight: 400; line-height: 34px; color: var(--white);
  }
  .tagline-band b { font-weight: 600; }
  .contact-strip {
    position: absolute; left: 0; top: 433px; width: 500px; height: 47px;
    background: var(--white);
    display: flex; align-items: center; gap: 18px; padding-left: 20px;
    font-size: 15.5px; font-weight: 600; color: var(--olive-text);
  }
  .contact-strip .label { color: #5b5b4a; }
</style>
</head>
<body>

  <section class="card card-back">
    <div class="brand-back"><span class="brand-mark"></span>Harborview Realty</div>
    <p class="testimonial">"Dale is absolutely the best. Selling our home was so much easier with him as our realtor. He is always there to answer questions no matter how small. I would definition recommend him!"</p>
    <p class="testimonial-name">Nora Kessler</p>
    <p class="testimonial-meta">HR Client - 4/13/2015</p>
    <div class="home-photos" role="img" aria-label="Three photographs of suburban homes for sale"></div>
    <div class="rated-band">Top Rated Realtors</div>
    <div class="edge-tab"></div>
  </section>

  <section class="card card-front">
    <div class="scene" role="img" aria-label="Sepia photograph of a mountain lake landscape"></div>
    <div class="portrait" role="img" aria-label="Portrait photograph of the realtor"></div>
    <div class="brand-front"><span class="brand-mark"></span>Harborview Realty</div>
    <ul class="selling-points">
      <li><b>LOCAL</b>Colorado Springs and Falcon Experts</li>
      <li>Over&nbsp;<b>9 YEARS</b>of experience</li>
      <li><b>LOW</b>commissions</li>
      <li>Homes selling&nbsp;<b>FAST</b>and at&nbsp;<b>TOP DOLLAR</b></li>
      <li><b>FREE</b>expert pricing opinions and Consultations</li>
    </ul>
    <div class="tagline-band">Never Merely Own a House.<br><b>THRIVE</b> at Harborview.</div>
    <div class="contact-strip">
      <span><span class="label">T:</span> 482-630-9157</span>
      <span><span class="label">W:</span> thriveatharborview.com</span>
    </div>
  </section>

</body>
</html>
```